Tranquil Pathway Business Card

Logo attached. (will be printing onto thick white/off white textured card)

Double sided business card for two Therapists working at Tranquil Pathway.

Require one design, but with different name and mobile numbers on each card.

Target Market(s)

Medical, Health

Industry/Entity Type

Business

Contact Information for Business Card

Need one business card design, but a separate card for each person - Colin Marchetti and Marieke de Boeckx.

FRONT OF CARD

Logo

Name (Colin Marchetti on one card, Marieke de Boeckx on the other)
Professional Clinical Hypnotherapist

Consulting Rooms (Near Lindqvist Hospital)
482 Brackenfield Road
Dunmore VIC 3987

Colin@TranquilPathway.example.au OR Marieke@TranquilPathway.example.au

Mobile: 0455 872 604 (for Colin) OR
Mobile: 0467 290 518 (for Marieke)

BACK OF CARD

Logo

Website: www.TranquilPathway.example.au

Phone: 1300 958 471

Requirements
Must have
• Text and logo only. No additiional graphics.

```html
<!DOCTYPE html>
<html lang="en">
<head>
<meta charset="utf-8">
<title>Tranquil Pathway Business Card</title>
<link rel="stylesheet" href="https://fonts.googleapis.com/css2?family=Montserrat:wght@700&family=Open+Sans:wght@400;600&display=swap">
<style>
  :root {
    --navy: #1f2a63;
    --grey: #5f5f63;
    --faint: #e9eaf0;
    --paper: #ffffff;
    --backdrop: #2b2b2d;
  }
  * { margin: 0; padding: 0; box-sizing: border-box; }
  html, body { width: 1200px; height: 900px; overflow: hidden; }
  body { background: var(--backdrop); position: relative; font-family: "Open Sans", sans-serif; }

  .card {
    position: absolute;
    width: 620px; height: 378px;
    background: var(--paper);
    border-radius: 22px;
    overflow: hidden;
    box-shadow: 0 14px 30px rgba(0,0,0,.45);
  }
  .card--logo-side { left: 60px; top: 60px; }
  .card--contact-side { left: 520px; top: 462px; }

  /* logo side */
  .faint-disc {
    position: absolute; width: 330px; height: 330px; border-radius: 50%;
    background: var(--faint); right: -110px; top: -70px;
  }
  .brand {
    position: absolute; left: 70px; top: 130px;
    display: flex; align-items: center; gap: 20px;
  }
  .brand__disc {
    width: 96px; height: 96px; border-radius: 50%; background: var(--navy);
    border: 8px solid var(--grey);
  }
  .brand__rule { width: 2px; height: 110px; background: var(--grey); }
  .wordmark {
    font-family: "Montserrat", sans-serif; font-weight: 700;
    color: var(--navy); text-transform: uppercase; line-height: 1.05;
  }
  .brand .wordmark { font-size: 34px; }
  .logo-side__contact {
    position: absolute; right: 40px; bottom: 44px; text-align: right;
    color: var(--grey); font-size: 15px; line-height: 1.6;
  }
  .logo-side__contact .site span { color: var(--navy); font-weight: 600; }

  /* contact side */
  .name-disc {
    position: absolute; width: 380px; height: 380px; border-radius: 50%;
    background: var(--navy); left: 200px; top: -170px;
  }
  .person {
    position: absolute; right: 100px; top: 116px; text-align: right; color: #fff;
  }
  .person__name { font-family: "Montserrat", sans-serif; font-weight: 700; font-size: 22px; letter-spacing: .5px; }
  .person__role { font-size: 10px; letter-spacing: .6px; margin-top: 2px; }
  .address {
    position: absolute; right: 36px; top: 224px; text-align: right;
    color: var(--navy); font-size: 14px; line-height: 1.45;
  }
  .contact-side__brand {
    position: absolute; left: 34px; top: 210px; font-size: 30px;
  }
  .details {
    position: absolute; left: 34px; bottom: 24px; list-style: none;
    color: var(--navy); font-size: 14px; line-height: 1.55;
  }
  .details li { display: flex; align-items: center; gap: 8px; }
  .details svg { width: 12px; height: 12px; fill: var(--navy); flex: none; }
</style>
</head>
<body>

<section class="card card--logo-side" aria-label="Card back">
  <div class="faint-disc"></div>
  <div class="brand">
    <div class="brand__disc"></div>
    <div class="brand__rule"></div>
    <div class="wordmark">Tranquil<br>Pathway</div>
  </div>
  <div class="logo-side__contact">
    <div class="phone">&#9742; 1300 958 471</div>
    <div class="site">www.<span>TranquilPathway</span>.example.au</div>
  </div>
</section>

<section class="card card--contact-side contact-side" aria-label="Card front">
  <div class="name-disc"></div>
  <div class="person">
    <div class="person__name">COLIN MARCHETTI</div>
    <div class="person__role">PROFESSIONAL CLINICAL HYPNOTHERAPIST</div>
  </div>
  <div class="address">Consulting Rooms (Near Lindqvist Hospital)<br>482 Brackenfield Road<br>Dunmore VIC 3987</div>
  <div class="wordmark contact-side__brand">Tranquil<br>Pathway</div>
  <ul class="details">
    <li><svg viewBox="0 0 12 12"><rect x="3" y="0" width="6" height="12" rx="1.2"/><rect x="4" y="1.5" width="4" height="7.5" fill="#fff"/></svg>0455 872 604</li>
    <li><svg viewBox="0 0 12 12"><rect x="0" y="2" width="12" height="8" rx="1"/><path d="M1 3l5 4 5-4" stroke="#fff" stroke-width="1" fill="none"/></svg>Colin@TranquilPathway.example.au</li>
    <li><svg viewBox="0 0 12 12"><circle cx="6" cy="6" r="6"/><path d="M0 6h12M6 0v12" stroke="#fff" stroke-width=".8"/></svg>www.TranquilPathway.example.au</li>
  </ul>
</section>

</body>
</html>
```